AI Startup Squarespace Website Design

I have a squarespace account setup with a domain name but need support to get the site looking good and launched. I will provide all text content and navigation/site map info. My company is working with clients to get business value out of Artificial Intelligence that helps automate processes, increase sales and improve customer customer experience. Leveraging the proven T.Helm AI Platform, our clients can get in-year benefits using customer service chatbots and other pre-built successful bots for automating/streamlining business processes in HR, accounting, underwriting, sales, training, remittances, emails, etc.

Target Market(s)

middle-market and large companies in Financial Services, Travel, Consumer Products, Manufacturing markets. Target is companies who want go improve sales, reduce costs and improve customer experience.

Industry/Entity Type

Financial

Font styles to use
Sans Serif

Requirements
Must have
• Professional but not too corporate-y.

```html
<!DOCTYPE html>
<html lang="en">
<head>
<meta charset="utf-8">
<title>Velora — Artificial Intelligence</title>
<link href="https://fonts.googleapis.com/css2?family=Roboto:wght@400;500;700&family=Open+Sans:ital,wght@0,400;0,600;1,400&display=swap" rel="stylesheet">
<style>
:root{
  --blue:#1f7fc4;
  --blue-deep:#0d3d78;
  --blue-bright:#2aa3dc;
  --accent:#1e9fd2;
  --ink:#222831;
  --text:#555b63;
  --muted:#8a9098;
  --white:#ffffff;
  --soft:#f3f4f6;
  --red:#d9452f;
  --dark:#1b1f26;
}
*{box-sizing:border-box;margin:0;padding:0}
html,body{width:1200px;height:3742px;overflow:hidden}
body{font-family:"Open Sans",Arial,sans-serif;color:var(--text);background:var(--white);position:relative}
h1,h2,h3,h4{font-family:"Roboto",Arial,sans-serif;color:var(--ink)}
.section{position:absolute;left:0;width:1200px}
.center{text-align:center}
.lead{font-size:13px;line-height:22px}

/* Hero */
.hero{top:0;height:680px;background:linear-gradient(100deg,#061a3a 0%,#0d3d78 35%,#1f6fbf 70%,#2c86d2 100%);overflow:hidden}
.hero-art{position:absolute;left:0;top:0;width:760px;height:620px;background:radial-gradient(circle at 300px 260px,rgba(120,200,255,.55) 0%,rgba(40,110,200,.25) 40%,rgba(10,40,90,0) 70%)}
.nav{position:absolute;top:32px;left:100px;right:100px;height:46px;display:flex;align-items:center}
.brand{display:flex;align-items:center;gap:12px;font-family:"Roboto",Arial,sans-serif;font-size:40px;font-weight:400;color:var(--white);letter-spacing:1px}
.brand-mark{width:36px;height:36px;border-radius:50%;background:var(--white)}
.menu{display:flex;gap:32px;margin-left:auto;align-items:center;font-family:"Roboto",Arial,sans-serif;font-size:15px;color:var(--white);font-weight:500}
.signin{border:2px solid var(--white);border-radius:4px;padding:7px 22px;margin-left:18px}
.hero-title{position:absolute;left:620px;top:370px;width:520px;text-align:right;font-family:"Roboto",Arial,sans-serif;font-weight:500;font-size:64px;line-height:66px;color:var(--white);text-shadow:0 2px 6px rgba(0,0,0,.35)}
.hero-dots{position:absolute;top:628px;left:565px;display:flex;gap:10px;align-items:center}
.hero-dots span{width:12px;height:12px;border-radius:50%;background:var(--white)}
.hero-dots span.on{width:18px;height:18px;border:3px solid var(--white);background:transparent}
.hero-curve{position:absolute;left:0;bottom:0;width:1200px;height:80px}

/* Services */
.services{top:680px;height:542px}
.title{font-size:36px;font-weight:500;letter-spacing:.5px}
.services .title{margin-top:62px}
.services .lead{width:660px;margin:18px auto 0}
.service-row{position:absolute;top:190px;left:90px;width:1020px;display:flex;justify-content:space-between}
.service{width:320px;text-align:center}
.service-icon{width:120px;height:120px;margin:0 auto;border-radius:50%;border:4px solid #d9e6f1;display:flex;align-items:center;justify-content:center}
.service-icon .disc{width:104px;height:104px;border-radius:50%;background:var(--accent);display:flex;align-items:center;justify-content:center}
.service h3{font-size:18px;font-weight:500;margin-top:46px;letter-spacing:.5px}
.service p{font-size:13px;line-height:22px;margin-top:10px}

/* About */
.about{top:1222px;height:445px;background:linear-gradient(100deg,#1b78bd 0%,#2a93d2 50%,#1c7dc0 100%)}
.about .title,.remit .title,.demo .title{color:var(--white)}
.about .title{margin-top:110px}
.about p{width:860px;margin:14px auto 0;color:var(--white);font-size:13px;line-height:22px}

/* Testimonial */
.testimonial{top:1667px;height:379px}
.testimonial .title{margin-top:94px}
.quote{width:780px;margin:22px auto 0;font-style:italic;font-size:13px;line-height:24px;color:var(--text)}
.author{margin-top:20px;font-style:italic;font-size:14px;color:var(--ink)}
.bars{display:flex;justify-content:center;gap:4px;margin-top:26px}
.bars span{width:26px;height:4px;background:#dcdfe3}
.bars span.on{background:var(--ink)}

/* Remittances */
.remit{top:2046px;height:444px;background:linear-gradient(110deg,#2a2f3a 0%,#3b4660 45%,#5a6478 70%,#2e3443 100%)}
.remit .title{margin-top:146px}
.remit p{width:860px;margin:14px auto 0;color:var(--white);font-size:13px;line-height:22px}

/* Blog */
.blog{top:2490px;height:434px}
.blog .title{margin-top:68px}
.post{position:absolute;top:168px;width:530px;display:flex;gap:25px}
.post-img{position:relative;width:212px;height:172px;flex:none}
.post-img.one{background:linear-gradient(135deg,#102a55,#2b6cc4 60%,#0a1c3d)}
.post-img.two{background:linear-gradient(135deg,#0b2f66,#2e8ddf 55%,#0c2a5a)}
.date{position:absolute;top:0;left:0;background:var(--accent);color:var(--white);font-size:12px;font-weight:600;padding:4px 10px}
.post h4{font-size:17px;font-weight:400;margin-top:14px}
.post p{font-size:13px;line-height:22px;margin-top:12px;width:280px}
.post a{display:inline-block;margin-top:6px;font-size:13px;color:var(--red);text-decoration:underline}

/* Demo */
.demo{top:2924px;height:407px;background:linear-gradient(110deg,#2b2520 0%,#4a3d33 40%,#3a352f 70%,#1f1c19 100%)}
.demo .title{margin-top:148px}
.btn{display:inline-block;margin-top:30px;width:237px;height:43px;line-height:43px;background:var(--accent);color:var(--white);font-family:"Roboto",Arial,sans-serif;font-weight:500;font-size:15px;letter-spacing:.5px}

/* Footer columns */
.info{top:3331px;height:332px}
.info h3{font-size:20px;font-weight:500;letter-spacing:.5px}
.newsletter{position:absolute;left:275px;top:62px;width:332px;text-align:center}
.newsletter p{font-size:12px;line-height:20px;margin-top:24px;padding:0 40px}
.field{margin-top:16px;height:44px;border:1px solid #d5d8dc;font-size:12px;line-height:44px;color:var(--muted)}
.sub{height:44px;background:var(--accent);color:var(--white);line-height:44px;font-family:"Roboto",Arial,sans-serif;font-weight:500;font-size:14px}
.contact{position:absolute;left:695px;top:62px;width:340px}
.contact ul{list-style:none;margin-top:28px}
.contact li{display:flex;gap:14px;font-size:13px;line-height:20px;margin-bottom:16px}
.contact svg{flex:none;margin-top:2px}
.social{display:flex;gap:8px}
.social span{width:26px;height:26px;border:2px solid var(--ink);border-radius:50%}
.footer{top:3663px;height:79px;background:var(--soft);text-align:center;font-size:12px;line-height:79px;color:var(--text)}
</style>
</head>
<body>

<header class="section hero">
  <div class="hero-art" role="img" aria-label="Glowing wireframe head with circuit rings, representing artificial intelligence"></div>
  <nav class="nav">
    <div class="brand"><span class="brand-mark"></span>velora</div>
    <div class="menu">
      <span>HOME</span><span>ABOUT US</span><span>SERVICES</span><span>WHAT WE DO</span><span>BLOG</span><span>CONTACT</span>
      <span class="signin">SIGN IN</span>
    </div>
  </nav>
  <h1 class="hero-title">ARTIFICIAL INTELLIGENCE</h1>
  <div class="hero-dots"><span class="on"></span><span></span><span></span><span></span></div>
  <svg class="hero-curve" viewBox="0 0 1200 80" preserveAspectRatio="none">
    <path d="M0 20 Q600 95 1200 0 L1200 80 L0 80 Z" fill="#ffffff"/>
    <path d="M0 20 Q600 95 1200 0" fill="none" stroke="#2aa3dc" stroke-width="4"/>
  </svg>
</header>

<section class="section services center">
  <h2 class="title">OUR SERVICES</h2>
  <p class="lead">Sed ut perspiciatis unde omnis iste natus error sit voluptatem accusantium doloremque laudantium, totam rem aperiam, eaque ipsa quae ab illo inore veritatis et quasi architecto beatae</p>
  <div class="service-row">
    <div class="service">
      <div class="service-icon"><div class="disc">
        <svg width="52" height="52" viewBox="0 0 52 52" fill="none" stroke="#fff" stroke-width="2.5"><rect x="8" y="6" width="26" height="36"/><rect x="18" y="14" width="26" height="34" fill="#1e9fd2"/><path d="M23 22h16M23 28h16M23 34h16M23 40h10"/></svg>
      </div></div>
      <h3>ACCOUNTING</h3>
      <p>Sed ut perspiciatis unde omnis iste natus error sit voluptatem accusantium doloremque laudantium, totam rem aperiam, eaque ipsa quae ab illo inore veritatis et quasi architecto beatae</p>
    </div>
    <div class="service">
      <div class="service-icon"><div class="disc">
        <svg width="52" height="52" viewBox="0 0 52 52" fill="none" stroke="#fff" stroke-width="2.5"><rect x="10" y="8" width="28" height="38" rx="2"/><path d="M18 8v-3h12v3M16 20h16M16 27h16M16 34h10"/><path d="M30 40l12-14 4 3-12 14-5 1z" fill="#1e9fd2"/></svg>
      </div></div>
      <h3>UNDERWRITING</h3>
      <p>Sed ut perspiciatis unde omnis iste natus error sit voluptatem accusantium doloremque laudantium, totam rem aperiam, eaque ipsa quae ab illo inore veritatis et quasi architecto beatae</p>
    </div>
    <div class="service">
      <div class="service-icon"><div class="disc">
        <svg width="52" height="52" viewBox="0 0 52 52" fill="#fff"><rect x="6" y="30" width="8" height="14"/><rect x="18" y="22" width="8" height="22"/><rect x="38" y="14" width="8" height="30"/><circle cx="32" cy="10" r="4"/><rect x="28" y="16" width="8" height="18"/><rect x="29" y="34" width="2.5" height="10"/><rect x="32.5" y="34" width="2.5" height="10"/><rect x="4" y="45" width="44" height="2.5"/></svg>
      </div></div>
      <h3>TRAINING</h3>
      <p>Sed ut perspiciatis unde omnis iste natus error sit voluptatem accusantium doloremque laudantium, totam rem aperiam, eaque ipsa quae ab illo inore veritatis et quasi architecto beatae</p>
    </div>
  </div>
</section>

<section class="section about center">
  <h2 class="title">ABOUT OUR COMPANY</h2>
  <p>Sed ut perspiciatis unde omnis iste natus error sit voluptatem accusantium doloremque laudantium, totam rem aperiam, eaque ipsa quae ab illo inventore veritatis et quasi architecto beatae vitae dicta sunt explicabo. Nemo enim ipsam voluptatem quia voluptas sit aspernatur aut odit aut fugit, sed quia consequuntur magni dolores eos qui ratione voluptatem sequi nesciunt.</p>
  <p>Nemo enim ipsam voluptatem quia voluptas sit aspernatur aut odit aut fugit, sed quia consequuntur magni dolores eos qui ratione voluptatem sequi nesciunt. Neque porro quisquam est, qui dolorem ipsum quia dolor sit amet, consectetur</p>
</section>

<section class="section testimonial center">
  <h2 class="title">CUSTOMER TESTIMONIAL</h2>
  <p class="quote">“ Sed ut perspiciatis unde omnis iste natus error sit voluptatem accusantium doloremque laudantium, totam rem aperiam, eaque ipsa quae ab illo inventore veritatis et quasi architecto beatae vitae dicta sunt explicabo. Nemo enim ipsam voluptatem quia voluptas sit aspernatur aut odit aut fugit, sed quia consequuntur .</p>
  <p class="author">John Doe - Velora</p>
  <div class="bars"><span class="on"></span><span></span><span></span></div>
</section>

<section class="section remit center" role="img" aria-label="Team working at a glass wall covered in sticky notes">
  <h2 class="title">REMITTANCES</h2>
  <p>Sed ut perspiciatis unde omnis iste natus error sit voluptatem accusantium doloremque laudantium, totam rem aperiam, eaque ipsa quae ab illo inventore veritatis et quasi architecto beatae vitae dicta sunt explicabo. Nemo enim ipsam voluptatem quia voluptas sit aspernatur aut odit aut fugit, sed quia consequuntur magni dolores eos qui ratione voluptatem sequi nesciunt.</p>
</section>

<section class="section blog">
  <h2 class="title center">LATEST BLOG</h2>
  <article class="post" style="left:100px">
    <div class="post-img one" role="img" aria-label="Person holding a tablet showing a glowing brain graphic"><span class="date">April 25, 2018</span></div>
    <div>
      <h4>Lorem Ipsum dolor sit amet</h4>
      <p>Nemo enim ipsam voluptatem quia voluptas sit aspernatur aut odit aut fugit, sed quia consequuntur magni dolores eos qui ratione</p>
      <a>Learn More</a>
    </div>
  </article>
  <article class="post" style="left:646px">
    <div class="post-img two" role="img" aria-label="Abstract blue digital network sphere"><span class="date">April 28, 2018</span></div>
    <div>
      <h4>Lorem Ipsum dolor sit amet</h4>
      <p>Nemo enim ipsam voluptatem quia voluptas sit aspernatur aut odit aut fugit, sed quia consequuntur magni dolores eos qui ratione</p>
      <a>Learn More</a>
    </div>
  </article>
</section>

<section class="section demo center" role="img" aria-label="Colleagues gathered around a table in a meeting">
  <h2 class="title">CONTACT US FOR A FREE DEMO</h2>
  <span class="btn">REQUEST DEMO</span>
</section>

<section class="section info">
  <div class="newsletter">
    <h3>SIGN UP FOR NEWSLETTER</h3>
    <p>Excepteur sint occaecat cupidatat non proident, sunt in culpa qui officia deserunt</p>
    <div class="field">Enter email</div>
    <div class="sub">SUBSCRIPTION</div>
  </div>
  <div class="contact">
    <h3>CONTACT US</h3>
    <ul>
      <li><svg width="14" height="18" viewBox="0 0 14 18"><path d="M7 0a7 7 0 0 0-7 7c0 5 7 11 7 11s7-6 7-11a7 7 0 0 0-7-7z" fill="#1e9fd2"/><circle cx="7" cy="7" r="2.5" fill="#fff"/></svg><span>Velora<br>48 Linden Park Rd Fairhaven, NJ 07000</span></li>
      <li><svg width="16" height="16" viewBox="0 0 16 16"><path d="M3 1l3 3-2 2c1 2 3 4 6 6l2-2 3 3-2 2C7 15 1 9 1 3z" fill="#1e9fd2"/></svg><span>Phone: 1-800-555-0142</span></li>
      <li><svg width="16" height="12" viewBox="0 0 16 12"><rect width="16" height="12" fill="#1e9fd2"/><path d="M0 0l8 6 8-6" fill="none" stroke="#fff" stroke-width="1.5"/></svg><span>hello@velora.example</span></li>
    </ul>
    <div class="social"><span></span><span></span><span></span><span></span></div>
  </div>
</section>

<footer class="section footer">©2018 Velora . All Rights Reserved.</footer>

</body>
</html>
```